Maple Bug Guard Business Cards

A modern business card with a predominantly white background and a sleek design featuring Maple with complimentary greys or blacks to convey a professional and contemporary look.

Front:
Primarily white background. Limited use of company purple color can be neighbored by greys.
Text: Name, Title, Cell Phone, Office Phone, Website, email address

Back:
Background Continuation: The back of the card maintains the white background for consistency.
Company name “Maple” in company color and font, “Bug Guard” underneath or underneath left justified of “Maple.”
A subtle pattern or texture in shades of grey to add depth behind the company Logo in font.

logo color: hex #6212ab
font: antique olive nord D Regular

```html
<!DOCTYPE html>
<html lang="en">
<head>
<meta charset="utf-8">
<title>Maple Bug Guard Business Card</title>
<link rel="stylesheet" href="https://fonts.googleapis.com/css2?family=Archivo:wght@700;800&display=swap">
<style>
  :root {
    --brand: #6212ab;
    --frame-edge: #c49af6;
    --frame-mid: #f6effe;
    --card: #ffffff;
    --field: #dedede;
    --ink: #111111;
    --mark-tint: #e7dcf3;
  }
  html, body {
    margin: 0;
    padding: 0;
    width: 1200px;
    height: 704px;
    overflow: hidden;
    background: #ffffff;
  }
  .card {
    position: relative;
    width: 1200px;
    height: 704px;
    background: linear-gradient(90deg, var(--frame-edge) 0%, var(--frame-mid) 50%, var(--frame-edge) 100%);
    font-family: "Archivo", Arial, sans-serif;
  }
  .card-face {
    position: absolute;
    left: 23px;
    top: 23px;
    right: 23px;
    bottom: 23px;
    background: var(--card);
  }
  .contact-field {
    position: absolute;
    left: 0;
    width: 718px;
    height: 79px;
    background: var(--field);
    display: flex;
    align-items: center;
    padding-left: 102px;
    box-sizing: border-box;
    color: var(--ink);
    font-weight: 800;
    font-size: 27px;
    font-variant: small-caps;
    letter-spacing: 0.5px;
  }
  .field-name    { top: 25px; }
  .field-title   { top: 132px; }
  .field-cell    { top: 238px; }
  .field-office  { top: 341px; }
  .field-web     { top: 447px; }
  .field-email   { top: 553px; padding-left: 106px; font-size: 26px; }
  .brand-dot {
    position: absolute;
    left: 878px;
    top: 190px;
    width: 118px;
    height: 118px;
    border-radius: 50%;
    background: var(--mark-tint);
  }
  .brand-name {
    position: absolute;
    right: 53px;
    top: 330px;
    text-align: right;
    color: var(--brand);
    font-weight: 800;
    line-height: 1;
  }
  .brand-primary {
    display: block;
    font-size: 92px;
    letter-spacing: 2px;
    font-variant: small-caps;
  }
  .brand-secondary {
    display: block;
    margin-top: 8px;
    font-size: 25px;
    font-variant: small-caps;
    letter-spacing: 0.5px;
  }
</style>
</head>
<body>
  <div class="card">
    <div class="card-face">
      <div class="contact-field field-name">Your Name</div>
      <div class="contact-field field-title">Your Title</div>
      <div class="contact-field field-cell">Cell Phone</div>
      <div class="contact-field field-office">Office Phone</div>
      <div class="contact-field field-web">Website</div>
      <div class="contact-field field-email">email address</div>

      <div class="brand-dot"></div>
      <div class="brand-name">
        <span class="brand-primary">Maple</span>
        <span class="brand-secondary">Bug Guard</span>
      </div>
    </div>
  </div>
</body>
</html>
```